Velmora and Co Business Card Design

Looking for a business card design. Wanting Smart, Clean and Sharp looking to promote Velmora and Co, our Import Export Business - like Black, White and natural textures. I have uploaded our logo. I like a rounded font but open to other ideas
Being that we have a wide range of products on offer we are looking for a neutral yet eye catching card. We would also like to have Import - Export on the business card to be clear on want our business does.

Target Market(s)

Import export market

Industry/Entity Type

Importer

Contact Information for Business Card

Mr Tobias Kernwell
tobias.kernwell@velmoraandco.com.au
+61 (0) 417 630 284
www.velmoraandco.com.au

Font styles to use
Other font styles liked:
• Unsure of actual font name but something rounded and clean

Colors

Designer to choose colors to be used in the design.

Requirements
Must have
• Instagram icon
• Facebook icon

```html
<!DOCTYPE html>
<html lang="en">
<head>
<meta charset="utf-8">
<title>Velmora and Co Business Card</title>
<link href="https://fonts.googleapis.com/css2?family=Bebas+Neue&family=Lato:wght@400&display=swap" rel="stylesheet">
<style>
  :root {
    --backdrop: #2a2a2a;
    --card: #1f1f20;
    --card-pattern: #262627;
    --ink: #ffffff;
    --ink-soft: #e3e5e4;
    --ink-muted: #b9bbba;
    --rule: #6a6a6a;
  }
  html, body {
    margin: 0;
    padding: 0;
    width: 1200px;
    height: 1108px;
    overflow: hidden;
    background: var(--backdrop);
  }
  .stage {
    position: relative;
    width: 1200px;
    height: 1108px;
  }
  .card {
    position: absolute;
    top: 234px;
    width: 400px;
    height: 640px;
    background: var(--card);
    border-radius: 26px;
    box-shadow: 0 18px 40px rgba(0,0,0,0.45);
    overflow: hidden;
    box-sizing: border-box;
  }
  .card--front { left: 150px; }
  .card--back { left: 650px; }

  .brand-mark {
    display: flex;
    align-items: center;
    justify-content: center;
    gap: 14px;
    font-family: "Bebas Neue", sans-serif;
    color: var(--ink-soft);
    letter-spacing: 1px;
    line-height: 1;
  }
  .brand-mark__square {
    width: 22px;
    height: 22px;
    background: var(--ink-soft);
  }
  .card--front .brand-mark {
    margin-top: 150px;
    font-size: 54px;
  }
  .holder-name {
    margin: 88px 0 0;
    text-align: center;
    font-family: "Bebas Neue", sans-serif;
    font-weight: 400;
    font-size: 34px;
    line-height: 1;
    color: var(--ink);
    letter-spacing: 1px;
  }
  .trade-line {
    margin-top: 6px;
    text-align: center;
    font-family: "Lato", sans-serif;
    font-size: 13px;
    letter-spacing: 3px;
    text-transform: uppercase;
    color: var(--ink-muted);
  }
  .divider {
    display: flex;
    align-items: center;
    gap: 8px;
    width: 250px;
    margin: 12px auto 0;
  }
  .divider::before, .divider::after {
    content: "";
    flex: 1;
    height: 1px;
    background: var(--rule);
  }
  .icon-tile {
    width: 22px;
    height: 22px;
    display: block;
  }
  .contact {
    margin-top: 8px;
    text-align: center;
    font-family: "Lato", sans-serif;
    font-size: 17px;
    line-height: 23px;
    color: var(--ink);
  }
  .divider--social { margin-top: 16px; width: 300px; }
  .social-handle {
    display: flex;
    align-items: center;
    gap: 6px;
    font-family: "Lato", sans-serif;
    font-size: 13px;
    color: var(--ink);
    white-space: nowrap;
  }
  .social-handle__square {
    width: 12px;
    height: 12px;
    background: var(--ink);
  }

  .pattern-field {
    position: absolute;
    left: 0;
    top: 0;
    width: 400px;
    height: 640px;
    background: linear-gradient(180deg, var(--card-pattern), var(--card) 85%);
  }
  .card--back .brand-mark {
    position: absolute;
    left: 0;
    right: 0;
    bottom: 110px;
    font-size: 54px;
  }
</style>
</head>
<body>
<main class="stage">
  <section class="card card--front" aria-label="Card front">
    <div class="brand-mark">
      <span class="brand-mark__square"></span>
      <span>Velmora &amp; Co</span>
    </div>
    <h1 class="holder-name">Mr Tobias Kernwell</h1>
    <div class="trade-line">Import - Export</div>
    <div class="divider">
      <svg class="icon-tile" viewBox="0 0 22 22" aria-label="Phone">
        <rect width="22" height="22" fill="#fff"/>
        <path d="M7 5 L9 5 L10 8 L8.5 9.5 Q10 12.5 12.5 13.5 L14 12 L17 13 L17 15 Q16 17 14 17 Q6 15 5 7 Q5 5 7 5 Z" fill="#1f1f20"/>
      </svg>
      <svg class="icon-tile" viewBox="0 0 22 22" aria-label="Email">
        <rect width="22" height="22" fill="#fff"/>
        <rect x="4" y="6" width="14" height="10" fill="none" stroke="#1f1f20" stroke-width="1.6"/>
        <path d="M4 6 L11 12 L18 6" fill="none" stroke="#1f1f20" stroke-width="1.6"/>
      </svg>
      <svg class="icon-tile" viewBox="0 0 22 22" aria-label="Website">
        <rect width="22" height="22" fill="#fff"/>
        <circle cx="11" cy="11" r="6.5" fill="none" stroke="#1f1f20" stroke-width="1.6"/>
        <path d="M4.5 11 H17.5 M11 4.5 Q7 11 11 17.5 M11 4.5 Q15 11 11 17.5" fill="none" stroke="#1f1f20" stroke-width="1.2"/>
      </svg>
    </div>
    <div class="contact">
      <div>+61 (0) 417 630 284</div>
      <div>tobias.kernwell@velmoraandco.com.au</div>
      <div>www.velmoraandco.com.au</div>
    </div>
    <div class="divider divider--social">
      <span class="social-handle" aria-label="Social page">
        <span class="social-handle__square"></span>/velmoraandco
      </span>
      <span class="social-handle" aria-label="Photo profile">
        <span class="social-handle__square"></span>@velmoraandco
      </span>
    </div>
  </section>

  <section class="card card--back" aria-label="Card back">
    <div class="pattern-field" role="img" aria-label="Faint repeating brand pattern across the card back"></div>
    <div class="brand-mark">
      <span class="brand-mark__square"></span>
      <span>Velmora &amp; Co</span>
    </div>
  </section>
</main>
</body>
</html>
```